Vex Pim ORA Need a custom graphic

I need to have the attached chart re-designed in a hand colored pencil format. The heading needs to be changed to "The most effective methods for hiring sales people". Do not include the background logo in the sample file.

Place the attached Vex Pim ORA logo next to the most effective methods (91%)

```html
<!DOCTYPE html>
<html lang="en">
<head>
<meta charset="utf-8">
<title>The Most Effective Methods for Hiring Sales People</title>
<link rel="stylesheet" href="https://fonts.googleapis.com/css2?family=Arimo:wght@700&family=Montserrat:wght@700;800&display=swap">
<style>
  :root {
    --navy: #06306f;
    --navy-soft: #2a4f8f;
    --sky: #0a9ae0;
    --ink: #111111;
    --grid: #5a5a5a;
    --line: #e04a1b;
    --line-soft: #f07a4f;
    --paper: #ffffff;
  }
  html, body {
    margin: 0;
    padding: 0;
    width: 1200px;
    height: 808px;
    overflow: hidden;
    background: var(--paper);
  }
  .canvas { position: relative; width: 1200px; height: 808px; background: var(--paper); }
  .chart { position: absolute; left: 0; top: 0; }
  .header-band { fill: var(--navy); }
  .header-hatch { stroke: var(--navy-soft); stroke-width: 1.4; opacity: 0.55; }
  .header-title {
    font-family: "Arimo", Arial, sans-serif;
    font-weight: 700;
    font-size: 29px;
    fill: #ffffff;
  }
  .grid-line { stroke: var(--grid); stroke-width: 1.1; fill: none; }
  .axis-value {
    font-family: "Montserrat", Arial, sans-serif;
    font-weight: 800;
    font-size: 21px;
    fill: var(--ink);
  }
  .axis-title-y {
    font-family: "Montserrat", Arial, sans-serif;
    font-weight: 800;
    font-size: 31px;
    fill: var(--navy);
  }
  .axis-title-x {
    font-family: "Montserrat", Arial, sans-serif;
    font-weight: 800;
    font-size: 32px;
    fill: var(--sky);
  }
  .trend { fill: none; stroke: var(--line); stroke-width: 4; stroke-linejoin: round; stroke-linecap: round; }
  .trend-shade { fill: none; stroke: var(--line-soft); stroke-width: 2; opacity: 0.7; stroke-linecap: round; }
  .trend-point { fill: var(--line); }
  .callout-box { fill: #ffffff; stroke: var(--ink); stroke-width: 2; }
  .callout-shade { fill: none; stroke: #444444; stroke-width: 0.8; opacity: 0.6; }
  .callout-text {
    font-family: "Montserrat", Arial, sans-serif;
    font-weight: 800;
    font-size: 14.5px;
    fill: var(--ink);
    letter-spacing: 0.6px;
  }
  .pointer { stroke: var(--line); stroke-width: 2; fill: none; }
  .pointer-head { fill: var(--line); }
  .brand-dot { fill: var(--navy); }
  .brand-name {
    font-family: "Montserrat", Arial, sans-serif;
    font-weight: 800;
    font-size: 15px;
    fill: var(--navy);
    letter-spacing: 0.6px;
  }
</style>
</head>
<body>
<div class="canvas">
<svg class="chart" width="1200" height="808" viewBox="0 0 1200 808" xmlns="http://www.w3.org/2000/svg">
  <defs>
    <filter id="pencil-rough" x="-5%" y="-5%" width="110%" height="110%">
      <feTurbulence type="fractalNoise" baseFrequency="0.05" numOctaves="2" seed="4" result="noise"/>
      <feDisplacementMap in="SourceGraphic" in2="noise" scale="2.6" xChannelSelector="R" yChannelSelector="G"/>
    </filter>
    <filter id="pencil-grain" x="0" y="0" width="100%" height="100%">
      <feTurbulence type="fractalNoise" baseFrequency="0.85" numOctaves="2" seed="7" result="grain"/>
      <feColorMatrix in="grain" type="matrix" values="0 0 0 0 0  0 0 0 0 0  0 0 0 0 0  0 0 0 -1.3 1.2" result="mask"/>
      <feComposite in="SourceGraphic" in2="mask" operator="in"/>
    </filter>
    <pattern id="pencil-hatch" width="7" height="7" patternUnits="userSpaceOnUse" patternTransform="rotate(35)">
      <line class="header-hatch" x1="0" y1="0" x2="0" y2="7"/>
    </pattern>
    <marker id="pointer-tip" viewBox="0 0 10 10" refX="9" refY="5" markerWidth="6" markerHeight="6" orient="auto">
      <path class="pointer-head" d="M0,0 L10,5 L0,10 L3,5 z"/>
    </marker>
  </defs>

  <!-- header -->
  <g class="header">
    <rect class="header-band" x="118.5" y="15.5" width="1049.5" height="74.5" filter="url(#pencil-grain)"/>
    <rect x="118.5" y="15.5" width="1049.5" height="74.5" fill="url(#pencil-hatch)" filter="url(#pencil-rough)"/>
    <text class="header-title" x="643" y="63" text-anchor="middle" textLength="1000" lengthAdjust="spacingAndGlyphs">THE MOST EFFECTIVE METHODS FOR HIRING SALES PEOPLE</text>
  </g>

  <!-- grid -->
  <g class="grid" filter="url(#pencil-rough)">
    <line class="grid-line" x1="119.5" y1="90" x2="119.5" y2="753"/>
    <line class="grid-line" x1="1168" y1="90" x2="1168" y2="753"/>
    <line class="grid-line" x1="215" y1="90" x2="215" y2="753"/>
    <line class="grid-line" x1="310" y1="90" x2="310" y2="753"/>
    <line class="grid-line" x1="405" y1="90" x2="405" y2="753"/>
    <line class="grid-line" x1="499" y1="90" x2="499" y2="753"/>
    <line class="grid-line" x1="594" y1="90" x2="594" y2="753"/>
    <line class="grid-line" x1="689" y1="90" x2="689" y2="753"/>
    <line class="grid-line" x1="783" y1="90" x2="783" y2="753"/>
    <line class="grid-line" x1="878" y1="90" x2="878" y2="753"/>
    <line class="grid-line" x1="973" y1="90" x2="973" y2="753"/>
    <line class="grid-line" x1="1068" y1="90" x2="1068" y2="753"/>
    <line class="grid-line" x1="119.5" y1="163" x2="1168" y2="163"/>
    <line class="grid-line" x1="119.5" y1="237" x2="1168" y2="237"/>
    <line class="grid-line" x1="119.5" y1="310" x2="1168" y2="310"/>
    <line class="grid-line" x1="119.5" y1="384" x2="1168" y2="384"/>
    <line class="grid-line" x1="119.5" y1="458" x2="1168" y2="458"/>
    <line class="grid-line" x1="119.5" y1="532" x2="1168" y2="532"/>
    <line class="grid-line" x1="119.5" y1="606" x2="1168" y2="606"/>
    <line class="grid-line" x1="119.5" y1="680" x2="1168" y2="680"/>
    <line class="grid-line" x1="119.5" y1="753" x2="1168" y2="753"/>
  </g>

  <!-- axis values -->
  <g class="axis-values">
    <text class="axis-value" x="64" y="117">0.90</text>
    <text class="axis-value" x="64" y="186">0.80</text>
    <text class="axis-value" x="64" y="258">0.70</text>
    <text class="axis-value" x="64" y="330">0.60</text>
    <text class="axis-value" x="64" y="403">0.50</text>
    <text class="axis-value" x="64" y="472">0.40</text>
    <text class="axis-value" x="64" y="541">0.30</text>
    <text class="axis-value" x="64" y="610">0.20</text>
    <text class="axis-value" x="64" y="680">0.10</text>
    <text class="axis-value" x="64" y="749">0.00</text>
  </g>
  <text class="axis-title-y" transform="translate(42 400) rotate(-90)" text-anchor="middle" filter="url(#pencil-grain)">PREDICTIVE VALIDITY</text>
  <text class="axis-title-x" x="598" y="789" text-anchor="middle" filter="url(#pencil-grain)">HIRING METHOD</text>

  <!-- trend line -->
  <g class="trend-group" filter="url(#pencil-rough)">
    <polyline class="trend" points="217.5,697 298,628 404,607 498,601 596,577 695,579 787,518 882,380 979,316 1074,220 1168,105"/>
    <polyline class="trend-shade" points="218,700 299,631 404,610 499,604 597,580 696,582 788,521 884,383 981,319 1076,223 1169,108"/>
    <circle class="trend-point" cx="217.5" cy="697" r="5.5"/>
    <circle class="trend-point" cx="298" cy="628" r="5.5"/>
    <circle class="trend-point" cx="404" cy="607" r="5.5"/>
    <circle class="trend-point" cx="498" cy="601" r="5.5"/>
    <circle class="trend-point" cx="596" cy="577" r="5.5"/>
    <circle class="trend-point" cx="695" cy="579" r="5.5"/>
    <circle class="trend-point" cx="787" cy="518" r="5.5"/>
    <circle class="trend-point" cx="882" cy="380" r="5.5"/>
    <circle class="trend-point" cx="979" cy="316" r="5.5"/>
    <circle class="trend-point" cx="1074" cy="220" r="5.5"/>
    <circle class="trend-point" cx="1168" cy="105" r="5.5"/>
  </g>

  <!-- pointers -->
  <g class="pointers" filter="url(#pencil-rough)">
    <line class="pointer" x1="1073" y1="135" x2="1108" y2="118" marker-end="url(#pointer-tip)"/>
    <line class="pointer" x1="980" y1="219" x2="1021" y2="218" marker-end="url(#pointer-tip)"/>
    <line class="pointer" x1="882" y1="310" x2="923" y2="310" marker-end="url(#pointer-tip)"/>
    <line class="pointer" x1="792" y1="380" x2="833" y2="380" marker-end="url(#pointer-tip)"/>
    <line class="pointer" x1="539" y1="475" x2="559" y2="509" marker-end="url(#pointer-tip)"/>
    <line class="pointer" x1="366" y1="548" x2="391" y2="578" marker-end="url(#pointer-tip)"/>
    <line class="pointer" x1="263" y1="598" x2="288" y2="627" marker-end="url(#pointer-tip)"/>
    <line class="pointer" x1="527" y1="655" x2="507" y2="622" marker-end="url(#pointer-tip)"/>
    <line class="pointer" x1="734" y1="655" x2="713" y2="623" marker-end="url(#pointer-tip)"/>
    <line class="pointer" x1="818" y1="561" x2="798" y2="528" marker-end="url(#pointer-tip)"/>
    <line class="pointer" x1="254" y1="728" x2="222" y2="704" marker-end="url(#pointer-tip)"/>
  </g>

  <!-- callout frames -->
  <g class="callout-frames" filter="url(#pencil-rough)">
    <rect class="callout-box" x="567" y="115" width="506" height="34"/>
    <rect class="callout-shade" x="569" y="117" width="502" height="30"/>
    <rect class="callout-box" x="616" y="194" width="362" height="34"/>
    <rect class="callout-shade" x="618" y="196" width="358" height="30"/>
    <rect class="callout-box" x="396" y="290" width="486" height="34"/>
    <rect class="callout-shade" x="398" y="292" width="482" height="30"/>
    <rect class="callout-box" x="502" y="366" width="290" height="34"/>
    <rect class="callout-shade" x="504" y="368" width="286" height="30"/>
    <rect class="callout-box" x="471" y="441" width="239" height="34"/>
    <rect class="callout-shade" x="473" y="443" width="235" height="30"/>
    <rect class="callout-box" x="162" y="512" width="305" height="34"/>
    <rect class="callout-shade" x="164" y="514" width="301" height="30"/>
    <rect class="callout-box" x="132" y="563" width="181" height="34"/>
    <rect class="callout-shade" x="134" y="565" width="177" height="30"/>
    <rect class="callout-box" x="811" y="562" width="181" height="34"/>
    <rect class="callout-shade" x="813" y="564" width="177" height="30"/>
    <rect class="callout-box" x="366" y="658" width="271" height="34"/>
    <rect class="callout-shade" x="368" y="660" width="267" height="30"/>
    <rect class="callout-box" x="685" y="658" width="271" height="34"/>
    <rect class="callout-shade" x="687" y="660" width="267" height="30"/>
    <rect class="callout-box" x="255" y="714" width="179" height="35"/>
    <rect class="callout-shade" x="257" y="716" width="175" height="31"/>
  </g>

  <!-- callout labels -->
  <g class="callout-labels">
    <text class="callout-text" x="820" y="137" text-anchor="middle" textLength="458" lengthAdjust="spacingAndGlyphs">SALES-SPECIFIC MULTI-MEASUREMENT ASSESSMENT, 91%</text>
    <text class="callout-text" x="797" y="216" text-anchor="middle" textLength="326" lengthAdjust="spacingAndGlyphs">MULTI-MEASUREMENT ASSESSMENT, 71%</text>
    <text class="callout-text" x="639" y="312" text-anchor="middle" textLength="442" lengthAdjust="spacingAndGlyphs">HIGHLY STRUCTURED INTERVIEW WITH SCRECARD, 57%</text>
    <text class="callout-text" x="647" y="388" text-anchor="middle" textLength="250" lengthAdjust="spacingAndGlyphs">GENERAL MENTAL ABILITY, 51%</text>
    <text class="callout-text" x="590.5" y="463" text-anchor="middle" textLength="195" lengthAdjust="spacingAndGlyphs">REFERENCE CHECK, 23%</text>
    <text class="callout-text" x="314.5" y="534" text-anchor="middle" textLength="286" lengthAdjust="spacingAndGlyphs">BEHAVIOR/ PERSONALITY TEST, 20%</text>
    <text class="callout-text" x="222.5" y="585" text-anchor="middle" textLength="107" lengthAdjust="spacingAndGlyphs">RESUME, 18%</text>
    <text class="callout-text" x="901.5" y="584" text-anchor="middle" textLength="136" lengthAdjust="spacingAndGlyphs">SKILLS TEST,33%</text>
    <text class="callout-text" x="501.5" y="680" text-anchor="middle" textLength="251" lengthAdjust="spacingAndGlyphs">TREADITIONAL INTERVIEW, 20%</text>
    <text class="callout-text" x="820.5" y="680" text-anchor="middle" textLength="254" lengthAdjust="spacingAndGlyphs">EMOTIONAL INTELLIGENCE, 23%</text>
    <text class="callout-text" x="344.5" y="736" text-anchor="middle" textLength="158" lengthAdjust="spacingAndGlyphs">CULTURE TEST, 13%</text>
  </g>

  <!-- brand beside the top method -->
  <g class="brand">
    <circle class="brand-dot" cx="990" cy="104" r="5"/>
    <text class="brand-name" x="1001" y="109">Vex Pim ORA</text>
  </g>
</svg>
</div>
</body>
</html>
```